Book cover for dissertation on learning in start-up teams

I am looking for a book cover (front, back, side) for publishing my phd project in A5 format. My phd Investigated the effects of learning (eg, reflection as a team, participation in team trainings) in start-up management teams on the performance and the satisfaction of synthesis teams. The front and side of the cover shoulderstand contain the name of the dissertation and my name, the back a short summary (see attachement). I am open with regard to the type of design (eg, photo, sketch, drawing) and with regard to the colors, etc.

Target Market(s)

Scientific community / Researchers and readers did are interested in team research

Industry/Entity Type

Learning

Requirements
Must have
• A5 format / pdf format / front, back, side

```html
<!DOCTYPE html>
<html lang="en">
<head>
<meta charset="utf-8">
<title>The Dissertation – On Learning in Start-up Teams</title>
<link rel="stylesheet" href="https://fonts.googleapis.com/css2?family=Tinos:wght@400;700&family=Exo+2:ital,wght@1,800&family=Arimo:wght@700&display=swap">
<style>
  :root {
    --stage: #3b3b3b;
    --back-panel: #6f6f79;
    --back-text: #f4f4f6;
    --spine-dark: #4a4a4a;
    --spine-light: #8a8a8a;
    --front-grey: #858585;
    --front-light: #ececec;
    --ink: #2b2b2b;
    --ink-soft: #1f1f1f;
    --photo-light: #d9dde2;
    --photo-mid: #8c96a3;
    --photo-dark: #2a3446;
  }
  html, body {
    margin: 0;
    padding: 0;
    width: 1200px;
    height: 772px;
    overflow: hidden;
    background: var(--stage);
  }
  .cover {
    position: relative;
    width: 1200px;
    height: 772px;
  }
  /* Back */
  .back {
    position: absolute;
    left: 35px;
    top: 22px;
    width: 543px;
    height: 726px;
    background: var(--back-panel);
    color: var(--back-text);
    font-family: "Tinos", "Times New Roman", serif;
  }
  .back__heading {
    position: absolute;
    top: 57px;
    left: 0;
    width: 100%;
    margin: 0;
    text-align: center;
    font-size: 19px;
    font-weight: 700;
  }
  .back__body {
    position: absolute;
    left: 84px;
    top: 87px;
    width: 400px;
    font-size: 14.6px;
    line-height: 17px;
  }
  .back__group { margin: 0 0 8px; }
  .back__signature {
    position: absolute;
    left: 84px;
    top: 629px;
    font-size: 14.6px;
    line-height: 17px;
  }
  .back__signer {
    position: absolute;
    right: 85px;
    top: 648px;
    font-size: 14.6px;
  }
  /* Spine */
  .spine {
    position: absolute;
    left: 578px;
    top: 22px;
    width: 42px;
    height: 726px;
    background: linear-gradient(90deg, var(--spine-dark), var(--spine-light) 55%, #6a6a6a);
  }
  .spine__title {
    position: absolute;
    left: 50%;
    top: 363px;
    transform: translate(-50%, -50%) rotate(90deg);
    white-space: nowrap;
    color: #ffffff;
    font-family: "Exo 2", "Arial Black", sans-serif;
    font-style: italic;
    font-weight: 800;
    font-size: 23px;
    letter-spacing: 0.5px;
  }
  /* Front */
  .front {
    position: absolute;
    left: 620px;
    top: 22px;
    width: 548px;
    height: 726px;
    background: var(--front-light);
    overflow: hidden;
  }
  .front__backdrop {
    position: absolute;
    left: 0;
    top: 0;
  }
  .front__institution {
    position: absolute;
    top: 130px;
    left: 90px;
    width: 390px;
    text-align: center;
    color: var(--ink-soft);
    font-family: "Tinos", "Times New Roman", serif;
  }
  .institution__name { font-size: 16px; line-height: 18px; }
  .institution__faculty { font-size: 15px; line-height: 18px; margin-bottom: 3px; }
  .institution__details { font-size: 9px; line-height: 11px; }
  .front__title {
    position: absolute;
    top: 360px;
    left: 0;
    width: 100%;
    margin: 0;
    text-align: center;
    color: var(--ink);
    font-family: "Exo 2", "Arial Black", sans-serif;
    font-style: italic;
    font-weight: 800;
    font-size: 56px;
    line-height: 70px;
    letter-spacing: 0;
    transform: scale(0.84, 1.2);
  }
  .front__subtitle {
    position: absolute;
    top: 430px;
    left: 0;
    width: 100%;
    margin: 0;
    text-align: center;
    color: var(--ink);
    font-family: "Arimo", Arial, sans-serif;
    font-weight: 700;
    font-size: 23px;
    letter-spacing: 0.3px;
  }
  .front__photo {
    position: absolute;
    left: 0;
    top: 488px;
    width: 548px;
    height: 238px;
    background:
      radial-gradient(ellipse at 78% 62%, #c7b8a8 0%, transparent 30%),
      radial-gradient(ellipse at 18% 80%, #b9a594 0%, transparent 28%),
      linear-gradient(100deg, var(--photo-light) 0%, var(--photo-mid) 45%, var(--photo-dark) 100%);
  }
</style>
</head>
<body>
<div class="cover">

  <section class="back">
    <h2 class="back__heading">Short abstract</h2>
    <div class="back__body">
      <p class="back__group">Drawing on two quantitative longitudinal studies, this<br>dissertation demonstrates the effects of</p>
      <p class="back__group">informal and formal learning activities on team outcomes in<br>founding teams and the mediating role</p>
      <p class="back__group">of teamwork quality. The effect of formal learning is shown<br>to be contingent on the extent of prior</p>
      <p class="back__group">informal learning. Moreover, this dissertation illustrates how<br>formal learning activities in form of a</p>
      <p class="back__group">team intervention for founding teams should be designed and<br>implemented. The results contribute</p>
      <p class="back__group">to diverse related areas of research.</p>
      <p class="back__group">Kurze Zusammenfassung</p>
      <p class="back__group">Aufbauend auf zwei quantitativen Studien zeigt diese<br>Dissertation die Wirkung von informalem</p>
      <p class="back__group">und formalem Lernen auf Teamergebnisse in Gründerteams<br>und beleuchtet, welche Rolle gute</p>
      <p class="back__group">Arbeitspraktiken im Team als vermittelnder Mechanismus<br>spielen. Der Effekt des formalen Lernens</p>
      <p class="back__group">hängt dabei von dem Ausmaß des vorherigen informalen<br>Lernens ab. Zudem erläutert diese</p>
      <p class="back__group">Dissertation, wie formales Lernen in Form einer Intervention<br>für Gründerteams konzipiert und</p>
      <p class="back__group">durchgeführt werden sollte. Die Ergebnisse leisten Beiträge<br>zu verschiedenen verwandten</p>
      <p class="back__group">Forschungszweigen.</p>
    </div>
    <div class="back__signature">Unterschrift ……………………………………………..</div>
    <div class="back__signer">(Prof. Dr. Dr. Keller)</div>
  </section>

  <section class="spine">
    <div class="spine__title">THE DISSERTATION</div>
  </section>

  <section class="front">
    <svg class="front__backdrop" width="548" height="488" viewBox="0 0 548 488" aria-hidden="true">
      <rect width="548" height="488" fill="var(--front-light)"/>
      <polygon points="0,0 220,0 0,348" fill="var(--front-grey)"/>
      <polygon points="310,0 548,0 548,348" fill="var(--front-grey)"/>
    </svg>
    <div class="front__institution">
      <div class="institution__name">TECHNISCHE UNIVERSITÄT LINDENAU</div>
      <div class="institution__faculty">Fakultät für Wirtschaftswissenschaften</div>
      <div class="institution__details">
        Department of Venture Studies and Management/Institute for Founder Team Research<br>
        Growing Together in New Ventures:<br>
        The Role of Team Reflection and a Training Programme<br>
        on Team Dynamics and Results Clara Weber<br>
        Vorsitzender: 1. Prof. Dr. Martin Falk<br>
        Prüfer der Dissertation 1. Prof. Dr. Dr. Jonas Keller&nbsp; 2. Prof. Dr. Lena Hartig
      </div>
    </div>
    <h1 class="front__title">THE DISSERTATION</h1>
    <p class="front__subtitle">ON LEARNING IN START-UP TEAMS</p>
    <div class="front__photo" role="img" aria-label="Photograph of business people's hands in suits holding a tablet and pen across a desk"></div>
  </section>

</div>
</body>
</html>
```